C U B A N - C I G A R S - F L Y E R

I need a double-sided 5x7 club type flyer for a Memorial Day Weekend Trip.
The main side design needs to be similar to the attached flyer example. The front design of flyer is KEY. The design will be awarded to the closest finished submission to the example flyer.
Both sides of the flyer should also included event and business logo, which are also attached. Both logos can be altered to fit printing need accordingly.
Front side content is also attached.
The back side design will be very simple. Consists of 3 travel images and trip description, and my contact very details. Same color design as front. The attached word document contains backside details for REFERENCE ONLY. Please focus on front side when submitting a design for this project.
Target Market(s)
A F R I C A N - A M E R I C A N - C I G A R - S M O K E R S
Industry/Entity Type
Travel Industry
Requirements
Must have
- All the elements of the attached information
Nice to have
- Masculine Images
Should not have
- Large Cigar focus to catch customer's attention

```html
<!DOCTYPE html>
<html lang="en">
<head>
<meta charset="utf-8">
<title>Cuba Cigar Memorial Day Weekend Flyer</title>
<link href="https://fonts.googleapis.com/css2?family=Archivo:wght@600;700;800;900&family=Open+Sans:wght@400;600&display=swap" rel="stylesheet">
<style>
  :root {
    --page-bg: #8c8c8c;
    --ember: #c4451f;
    --ember-soft: rgba(200, 72, 34, 0.82);
    --tobacco-dark: #3a1a0c;
    --tobacco: #8a4a1c;
    --leaf: #c98a3c;
    --parchment: #d9a653;
    --maroon: #5c1208;
    --cream: #fff6ea;
    --white: #ffffff;
    --ink: #2a1406;
  }
  * { box-sizing: border-box; margin: 0; padding: 0; }
  html, body { width: 1200px; height: 1200px; overflow: hidden; }
  body {
    background: var(--page-bg);
    font-family: "Archivo", Arial, sans-serif;
    position: relative;
  }
  .flyer {
    position: absolute;
    left: 236px;
    width: 726px;
    height: 518px;
    overflow: hidden;
    box-shadow: 0 6px 18px rgba(0,0,0,0.35);
  }
  .flyer--front { top: 67px; }
  .flyer--back { top: 632px; }
  .abs { position: absolute; }

  /* FRONT */
  .front-photo {
    inset: 0;
    background:
      radial-gradient(ellipse at 78% 55%, #e2b36a 0%, #b87a38 35%, #6e3515 75%, #3a1a0c 100%),
      var(--tobacco);
  }
  .front-side-panel {
    left: 0; top: 0; width: 268px; height: 518px;
    background: linear-gradient(180deg, var(--ember-soft) 0%, rgba(170,55,25,0.85) 45%, rgba(60,18,8,0.92) 75%, rgba(40,12,6,0.95) 100%);
  }
  .brand-mark {
    left: 60px; top: 17px; width: 172px; height: 172px;
    border: 2px solid var(--white);
    border-radius: 50%;
    display: flex; align-items: center; justify-content: center;
    text-align: center;
  }
  .brand-mark__name {
    font-weight: 700; font-size: 19px; line-height: 1.15;
    color: var(--white); letter-spacing: 0.06em;
  }
  .side-copy {
    left: 0; width: 292px; text-align: center;
    color: var(--white); font-weight: 700;
  }
  .side-copy--lead { top: 198px; font-size: 17px; line-height: 21px; }
  .side-copy--cigars { top: 241px; font-size: 20px; font-weight: 900; letter-spacing: 0.02em; }
  .side-copy--trip { top: 266px; font-size: 17px; line-height: 21.5px; }
  .side-rule { left: 34px; top: 342px; width: 216px; height: 2px; background: var(--white); }
  .weekend-stack { left: 33px; color: var(--white); font-weight: 900; line-height: 1; white-space: nowrap; }
  .weekend-stack--day { top: 357px; font-size: 24px; letter-spacing: 0.03em; }
  .weekend-stack--weekend { top: 385px; font-size: 38px; letter-spacing: 0.01em; }
  .weekend-stack--year { top: 424px; font-size: 66px; letter-spacing: -0.01em; }

  .headline { left: 284px; color: var(--maroon); font-weight: 800; line-height: 1; white-space: nowrap; }
  .headline--kicker { top: 43px; font-size: 21px; letter-spacing: 0.02em; }
  .headline--main { top: 66px; font-size: 45px; font-weight: 900; letter-spacing: 0.03em; }
  .headline--sub { top: 113px; font-size: 17.5px; font-weight: 700; }

  .event-badge {
    left: 289px; top: 158px; width: 174px; height: 174px;
    border: 3px solid var(--white);
    border-radius: 50%;
    display: flex; align-items: center; justify-content: center;
    text-align: center;
  }
  .event-badge__name {
    color: var(--white); font-weight: 900; font-size: 15px; line-height: 1.2;
    letter-spacing: 0.03em;
  }
  .event-info {
    right: 14px; max-width: 434px; text-align: right; color: var(--white); font-weight: 700;
    font-size: 17.5px; line-height: 1; white-space: nowrap;
  }
  .event-info--dates { top: 388px; }
  .event-info--book { top: 410px; }
  .event-info--call { top: 432px; }
  .book-button {
    left: 582px; top: 457px; width: 130px; height: 44px;
    border: 2px solid var(--white); border-radius: 12px;
    color: var(--white); text-align: center;
    display: flex; flex-direction: column; justify-content: center;
  }
  .book-button__main { font-size: 18px; font-weight: 800; line-height: 1.05; }
  .book-button__note { font-size: 11px; font-weight: 700; }

  /* BACK */
  .back-texture {
    inset: 0;
    background: radial-gradient(ellipse at 55% 60%, #e0a24e 0%, #c27e34 45%, #8a4a1c 85%, #6a3414 100%);
  }
  .back-cigar-fade {
    right: 0; top: 150px; width: 260px; height: 260px;
    background: radial-gradient(ellipse at 70% 50%, rgba(240,205,140,0.55), rgba(240,205,140,0) 70%);
  }
  .gallery-band {
    left: 76px; top: 26px; width: 560px; height: 230px;
    background: rgba(200, 72, 34, 0.78);
  }
  .gallery-frame {
    top: 37px; height: 109px;
    border: 4px solid var(--white);
  }
  .gallery-frame--cars { left: 96px; width: 154px; background: linear-gradient(135deg, #e44fa0 0%, #f2d23a 40%, #2a72d8 75%, #1a3d7a 100%); }
  .gallery-frame--map { left: 263px; width: 159px; background: linear-gradient(180deg, #eef4fb 0%, #cfe0f2 55%, #f2a22a 56%, #e9961f 70%, #d6e6f5 71%); }
  .gallery-frame--cigars { left: 433px; width: 173px; background: linear-gradient(160deg, #7a4524 0%, #a0643a 40%, #5a2e14 100%); }
  .trip-story {
    left: 98px; top: 157px; width: 510px;
    font-family: "Open Sans", Arial, sans-serif; font-size: 7.6px; line-height: 9.6px;
    color: var(--ink); text-align: justify;
  }
  .trip-story em { font-weight: 600; }
  .back-badge {
    left: 14px; top: 24px; width: 116px; height: 116px;
    border: 3px solid var(--white); border-radius: 50%;
    display: flex; align-items: center; justify-content: center; text-align: center;
    background: rgba(180, 70, 30, 0.55);
    z-index: 2;
  }
  .back-badge__name { color: var(--white); font-weight: 900; font-size: 10.5px; line-height: 1.2; }
  .back-brand {
    left: 618px; top: 158px; width: 100px; height: 100px;
    border: 2px solid var(--white); border-radius: 50%;
    display: flex; align-items: center; justify-content: center; text-align: center;
  }
  .back-brand__name { color: var(--white); font-weight: 700; font-size: 11px; line-height: 1.15; letter-spacing: 0.05em; }

  .detail-list { list-style: none; color: var(--ink); font-weight: 700; font-size: 11px; }
  .detail-list li { position: relative; padding-left: 10px; }
  .detail-list li::before {
    content: ""; position: absolute; left: 0; top: 4px; width: 5px; height: 5px; background: var(--ink);
  }
  .detail-list--costs { left: 96px; top: 275px; }
  .detail-list--costs li { line-height: 18.8px; }
  .included-title { left: 370px; top: 264px; font-size: 11px; font-weight: 700; color: var(--ink); }
  .detail-list--included { left: 360px; top: 278px; width: 320px; }
  .detail-list--included li { line-height: 14.4px; }
  .detail-list--included li::before { top: 4.5px; }
  .list-divider { left: 350px; top: 268px; width: 1.5px; height: 132px; background: var(--ink); }

  .deposit-band {
    left: 0; top: 424px; width: 726px; height: 94px;
    background: linear-gradient(180deg, rgba(200,72,34,0.9), rgba(150,48,20,0.95));
    color: var(--white); text-align: center;
  }
  .deposit-band__main { position: absolute; left: 0; right: 0; top: 12px; font-size: 24px; font-weight: 800; }
  .deposit-band__note { position: absolute; left: 0; right: 0; top: 42px; font-size: 16px; font-weight: 600; }
</style>
</head>
<body>

<section class="flyer flyer--front">
  <div class="abs front-photo" role="img" aria-label="Photo of a box of hand-rolled Cuban cigars with one lit cigar smoking"></div>
  <div class="abs front-side-panel" role="img" aria-label="Glass of red wine with autumn leaves under a warm orange tint"></div>

  <div class="abs brand-mark"><span class="brand-mark__name">HARBOR<br>TRAVEL CO</span></div>

  <p class="abs side-copy side-copy--lead">Legally travel to Cuba<br>and return with real</p>
  <p class="abs side-copy side-copy--cigars">CUBAN CIGARS!</p>
  <p class="abs side-copy side-copy--trip">TRIP NAME:<br>Rum Cigars and<br>Classic Cars</p>
  <div class="abs side-rule"></div>
  <p class="abs weekend-stack weekend-stack--day">MEMORIAL DAY</p>
  <p class="abs weekend-stack weekend-stack--weekend">WEEKEND</p>
  <p class="abs weekend-stack weekend-stack--year">2018!</p>

  <p class="abs headline headline--kicker">A CUBA GIGAR GENTELEMEN’S</p>
  <h1 class="abs headline headline--main">MEMORIAL DAY</h1>
  <p class="abs headline headline--sub">CIGARS,RUM,&amp; CLASSIC CARS.........</p>

  <div class="abs event-badge"><span class="event-badge__name">MEMORIAL DAY<br>WEEKEND<br>CUBA TRIP<br>MAY 25-28</span></div>

  <p class="abs event-info event-info--dates">DATES:FRIDAY,MAY 25TH - TUESDAY MAY 29TH</p>
  <p class="abs event-info event-info--book">Book Today at www.HARBORTC.COM/CUBA2018</p>
  <p class="abs event-info event-info--call">For MoreInformational Call XXX-XXX-XXXX</p>
  <div class="abs book-button">
    <span class="book-button__main">BOOK NOW</span>
    <span class="book-button__note">SPACE IS LIMITED</span>
  </div>
</section>

<section class="flyer flyer--back">
  <div class="abs back-texture" role="img" aria-label="Aged parchment texture in warm tobacco tones"></div>
  <div class="abs back-cigar-fade" role="img" aria-label="Faded cigars in the background"></div>
  <div class="abs gallery-band"></div>
  <div class="abs gallery-frame gallery-frame--cars" role="img" aria-label="Colourful classic American cars parked in Havana"></div>
  <div class="abs gallery-frame gallery-frame--map" role="img" aria-label="Map of the flight route from Miami to Havana, Cuba"></div>
  <div class="abs gallery-frame gallery-frame--cigars" role="img" aria-label="Close-up of premium Cuban cigars"></div>

  <div class="abs back-badge"><span class="back-badge__name">MEMORIAL DAY<br>WEEKEND<br>CUBA TRIP<br>MAY 25-28</span></div>

  <p class="abs trip-story">Cuba is the ultimate bucket list destination for any cigar lover. Now is your opportunity to legally travel to Cuba and experience a country that has been off limits to Americans for more than 50 years before it changes. Smoke fine Cuban cigars, meet its resilient people and experience Cuba’s fascinating culture. Tour cigar factories, watch expert cigar rollers, visit a humidor factory and workshop, tour the Old Harbor Rum Museum to learn firsthand the process of making rum followed by rum tasting and pairings with Cuban cigars in a private setting and much more. Explore the Pinar Del Rio located in the Viñales Valley known for its stunning landscapes and tobacco plantations. Visit the world famous Verde Leaf Tobacco Plantation to see first hand where and how the tobacco process is grown for fine Cuban Cigars. The bucket list trip of a lifetime awaits on this ‘people to people’ Cigar Journey to Cuba to learn first hand about Cuban cigars, meet the Cuban people, experience incredible cuisine, drive in classic American cars along the Malecón and experience the Cuban cigar process from <em>‘seed to smoke’</em> and an opportunity to smoke in the birthplace of cigars!</p>

  <div class="abs back-brand"><span class="back-brand__name">HARBOR<br>TRAVEL CO</span></div>

  <ul class="abs detail-list detail-list--costs">
    <li>Trip Cost: $2050</li>
    <li>Deposit: $300</li>
    <li>Payment plans available</li>
    <li>$300 Deposit Required</li>
    <li>Final payment Due By April 10, 2018</li>
    <li>*NON-REFUNDABLE</li>
    <li>*Passport Required</li>
  </ul>
  <div class="abs list-divider"></div>
  <p class="abs included-title">What’s Included:</p>
  <ul class="abs detail-list detail-list--included">
    <li>4 Days / 3 Nights</li>
    <li>5 Star Hotel Accommodations Based on Double Occupancy</li>
    <li>Roundtrip Coastline Air Tickets from Fort Lauderdale Florida - Cuba</li>
    <li>Tour Bus Chauffeured Transportation</li>
    <li>All Rum and Cigar Tour Events</li>
    <li>Select Meals (Breakfast, Welcome and Farewell Dinner) and More!</li>
  </ul>

  <div class="abs deposit-band">
    <p class="deposit-band__main">$300 Deposit Required Final payment Due By April 10, 2018</p>
    <p class="deposit-band__note">*NON-REFUNDABLE *Passport Required For More Information Call: XXX-XXX-XXXX</p>
  </div>
</section>

</body>
</html>
```